Weight gainer supplement design

Looking for a design for a weight gainer /meal replacement supplement. The black plastic tub we will use has 2 spaces for sticker one around the rim approx 2.8cm tall x 30cm wideAnother around the main tub. The main sticker size will be 18cm tall by 70cm this will include the front of the product then wrap around to show the nutritional table.The brand is KRV (Kestrel vigor works) and the product will be called ALPHA MASSThe target ordience is men aged 16-35 its should have a profesional feel to it. The product comes in a black tub, the colores we would like to use are black and blue or red or gold or silver but we are open to suggestions and would like artistic imput. Are logo for KRV is attached but can be changed if the designer prefers.Attached is 1. KRV logo2. Image of similar product that comes in the same tub3 - 5 - images of similar products that we like the design of.The product is 12lbs and will be vanilla flavor. Please ask for more suggestions if needed, I have kept this description short to try and get artistic input.Thanks in advance :)

Target Market(s)

18-35 males who go to the gym

Industry/Entity Type

Fitness

Colors

Designer to choose colors to be used in the design.

Requirements
Must have
• name titan bulk, logo KRV
Should not have
• images of people

```html
<!DOCTYPE html>
<html lang="en">
<head>
<meta charset="utf-8">
<title>TITAN BULK – Kestrel vigor works</title>
<link rel="stylesheet" href="https://fonts.googleapis.com/css2?family=Anton&family=Rajdhani:wght@500;600;700&family=Michroma&display=swap">
<style>
  :root{
    --stage:#d4d4d4;
    --label-black:#141414;
    --label-dark:#262729;
    --steel:#3a3c40;
    --band-blue:#2c4258;
    --band-deep:#16222f;
    --silver:#c9ccd0;
    --white:#ffffff;
  }
  *{margin:0;padding:0;box-sizing:border-box}
  html,body{width:1200px;height:1054px;overflow:hidden}
  body{background:var(--stage);font-family:"Rajdhani",sans-serif}
  .artboard{position:relative;width:1200px;height:1054px}
  .rim-sticker{position:absolute;left:150px;top:140px;width:900px;height:84px}
  .main-sticker{position:absolute;left:150px;top:290px;width:900px;height:600px}
  .rim-title{font-family:"Michroma",sans-serif;font-size:44px;fill:var(--white);letter-spacing:2px}
  .brand-name{font-family:"Michroma",sans-serif;font-size:92px;fill:var(--silver)}
  .product-name{font-family:"Anton",sans-serif;font-size:112px}
  .product-solid{fill:var(--white)}
  .product-outline{fill:none;stroke:var(--white);stroke-width:3}
  .tagline{font-family:"Rajdhani",sans-serif;font-weight:500;font-size:32px;fill:var(--white)}
  .stat-value{font-family:"Rajdhani",sans-serif;font-weight:700;font-size:34px;fill:var(--white)}
  .stat-unit{font-family:"Rajdhani",sans-serif;font-weight:600;font-size:13px;fill:var(--white);letter-spacing:1px}
  .stat-frame{fill:none;stroke:var(--white);stroke-width:3}
  .flavor{font-family:"Rajdhani",sans-serif;font-weight:700;font-size:36px;fill:#1b1c1e;stroke:var(--silver);stroke-width:1.2}
  .footer-text{font-family:"Rajdhani",sans-serif;font-weight:700;font-size:28px;fill:var(--white)}
</style>
</head>
<body>
<main class="artboard">

  <svg class="rim-sticker" viewBox="0 0 900 84" aria-label="Rim sticker">
    <defs>
      <linearGradient id="rimShade" x1="0" y1="0" x2="0" y2="1">
        <stop offset="0" stop-color="#2a2b2e"/>
        <stop offset="1" stop-color="#111"/>
      </linearGradient>
    </defs>
    <rect width="900" height="84" fill="url(#rimShade)"/>
    <text class="rim-title" x="450" y="58" text-anchor="middle">KESTREL&#160;&#160;VIGOR</text>
  </svg>

  <svg class="main-sticker" viewBox="0 0 900 600" aria-label="Main sticker, front panel">
    <defs>
      <linearGradient id="labelDark" x1="0" y1="0" x2="1" y2="1">
        <stop offset="0" stop-color="var(--label-dark)"/>
        <stop offset="0.6" stop-color="var(--steel)"/>
        <stop offset="1" stop-color="var(--label-black)"/>
      </linearGradient>
      <linearGradient id="bandBlue" x1="0" y1="0" x2="1" y2="0">
        <stop offset="0" stop-color="var(--band-deep)"/>
        <stop offset="0.35" stop-color="var(--band-blue)"/>
        <stop offset="0.75" stop-color="var(--band-deep)"/>
      </linearGradient>
    </defs>

    <rect class="label-body" width="900" height="600" fill="url(#labelDark)"/>

    <path class="accent-band" d="M0 300 L440 300 Q500 300 520 260 L520 600 L0 600 Z" fill="url(#bandBlue)"/>
    <rect class="footer-band" x="0" y="540" width="900" height="60" fill="var(--label-black)"/>

    <path class="sweep-line" d="M900 530 L700 530 Q650 530 620 550 L560 590 Q550 598 520 598 L0 598"
          fill="none" stroke="var(--white)" stroke-width="10"/>
    <path class="sweep-edge" d="M520 260 Q500 300 440 300 L0 300" fill="none" stroke="#5b6f84" stroke-width="2"/>

    <text class="brand-name" x="150" y="210">KRV</text>

    <g class="stat" transform="translate(150 262)">
      <path class="stat-frame" d="M0 12 L10 0 L74 0 L74 70 L0 70 Z"/>
      <text class="stat-value" x="37" y="40" text-anchor="middle">70g</text>
      <text class="stat-unit" x="37" y="60" text-anchor="middle">PROTEIN</text>
    </g>
    <g class="stat" transform="translate(150 348)">
      <path class="stat-frame" d="M0 12 L10 0 L74 0 L74 70 L0 70 Z"/>
      <text class="stat-value" x="37" y="40" text-anchor="middle">15g</text>
      <text class="stat-unit" x="37" y="60" text-anchor="middle">FATS</text>
    </g>
    <g class="stat" transform="translate(150 434)">
      <path class="stat-frame" d="M0 12 L10 0 L74 0 L74 70 L0 70 Z"/>
      <text class="stat-value" x="37" y="40" text-anchor="middle">900</text>
      <text class="stat-unit" x="37" y="60" text-anchor="middle">CALORIES</text>
    </g>

    <text class="flavor" x="240" y="478">VANILLA</text>
    <text class="flavor" x="240" y="512">FLAVOR</text>

    <text class="product-name product-solid" transform="translate(630 505) rotate(-90)">TITAN</text>
    <text class="product-name product-outline" transform="translate(728 505) rotate(-90)">BULK</text>
    <text class="tagline" transform="translate(766 505) rotate(-90)">High protein weight gain powder</text>

    <text class="footer-text" x="70" y="578">Net Wt 12lbs</text>
    <text class="footer-text" x="860" y="578" text-anchor="end">Dietary Supplement</text>
  </svg>

</main>
</body>
</html>
```